High-Converting Facebook Ads for Portals Drapes & Panels (6 Products)

We are looking for a graphic designer to create high-quality Facebook & Instagram ads for our business: Portals Drapes and Panels (Melbourne, Australia).

We require 6 separate ad designs, each for a different product:

Zipscreen Blinds

Outdoor Awnings

Plantation Shutters

Roller Shutters

Security Doors

Roller Blinds & Sheer Curtains

Ad Specifications:

Sizes:

1440 x 1800 px (4:5 ratio)

1080 x 1080 px (1:1 ratio)

1080 x 1920 px (9:16 ratio for Stories/Reels)

Format: PNG (high resolution, not blurry)

Designed specifically for Meta (Facebook/Instagram ads)

Mobile-friendly layout (clear, easy to read)

Style:

Bold, sales-driven, retail-style ads (NOT minimal)

Eye-catching and designed to generate leads

Clean, professional layout

Similar to promotional home improvement ads

Brand Colours:

Red: #E31E24

Blue: #0072BC

White backgrounds

Each ad must include:

“SALE NOW ON” banner at top

Our showroom address:
512 Upper Wattlebank Street, Fennick Vale (must be fully visible, not cut off)

Phone number: 9482 1576

Our logo (provided)

Badge: “Celebrating 13 YEARS in Business” (must be clean and readable)

Call to Action:

For 5 ads: “Book a FREE quote TODAY!”

For Security Doors ad: “ORDER NOW”

Offers / Pricing:

Most products: “UP TO 40% OFF”

Plantation Shutters: “FROM $299/sqm”

Security Doors: “FROM $750”

Content for each ad (examples):

Zipscreen Blinds:

Made to Measure

Fully Installed

Wind, Sun & Insect Protection

Outdoor Awnings:

Reduce Heat & Glare

Energy Saving

Custom Made

Plantation Shutters:

Modern & Elegant

Light & Privacy Control

Durable & Easy Care

Roller Shutters:

Security Protection

Block Heat & Noise

Total Light Control

Security Doors:

3 Point Locking

Premium Mesh

Custom Made

Blinds & Sheers:

Huge Range of Fabrics

Modern Soft Finish

Perfect for Any Room

Important Notes:

All text must be sharp and easy to read (no blur)

Layout must be balanced and not overcrowded

Ensure no text is cut off (especially address and headings)

Badge text must be straight and professional (no distortion)

Use high-quality, relevant images (we will provide references)

Goal:
Create ads that look professional, trustworthy, and generate enquiries/bookings for in-home quotes.

We are open to creative ideas but want a strong, bold retail-style ad that converts.
I have uploaed chatgpt mocks

Target Market(s)

Homeowners in Melbourne, Australia (typically aged 30–65) looking to improve their homes with blinds, shutters, awnings and security doors. Mid to high income households focused on quality, security, and modern home upgrades.

Industry/Entity Type

Home Improvement / Construction / Retail

Font styles to use
Sans Serif

Requirements
Must have
• Clear, bold and easy-to-read text (must be readable on mobile) High-quality, non-blurry design Strong “SALE” style layout (retail promotional look) Proper spacing (no overcrowded designs) All key info visible (address must NOT be cut off) Correct pricing and offers included Clean “13 YEARS” badge (no distortion or curved text) Consistent branding across all 6 ads
Nice to have
• Modern, slightly premium feel while still being bold Good use of contrast (red/blue/white) Subtle shadows or layering to improve depth Clean use of icons or bullet points Strong hierarchy (headline → benefits → offer → CTA) Variations in layout for testing different ad styles
Should not have
• Minimal or plain designs (we want bold, sales-driven ads) Hard-to-read fonts or script fonts Low-quality or blurry images Overcrowded layouts with too much text Important text cut off (especially address or headings) Overuse of effects or “cheap” looking graphics Yellow-heavy colour schemes (must follow brand colours)

```html
<!DOCTYPE html>
<html lang="en">
<head>
<meta charset="utf-8">
<title>Portals Drapes &amp; Panels – Sale Ad Set</title>
<link rel="stylesheet" href="https://fonts.googleapis.com/css2?family=Montserrat:wght@500;600;700;800;900&family=Oswald:wght@600;700&display=swap">
<style>
:root{
  --red:#e31e24;
  --red-deep:#c3141a;
  --blue:#0072bc;
  --blue-deep:#0b5c9b;
  --ink:#2a2a2a;
  --board:#5b5b5b;
  --paper:#ffffff;
  --paper-shade:#e9e9e9;
}
*{box-sizing:border-box;margin:0;padding:0}
html,body{width:1200px;height:3200px;overflow:hidden;background:var(--board)}
.board{position:relative;width:1200px;height:3200px;background:var(--board);font-family:'Montserrat',sans-serif;overflow:hidden}

.size-label{position:absolute;left:0;right:0;text-align:center;color:#fff;font-weight:800;font-size:44px;line-height:50px;letter-spacing:.01em}

/* ---------- shared ad parts ---------- */
.ad{position:absolute;overflow:hidden;background:linear-gradient(135deg,var(--paper) 0%,#f3f3f3 55%,var(--paper-shade) 100%);box-shadow:0 8px 18px rgba(0,0,0,.45)}
.ad>*{position:absolute}
.sq{width:320px;height:320px}
.st{width:283px;height:505px}
.pt{width:311px;height:392px}

.banner{left:0;top:0;background:linear-gradient(180deg,#ea2a30,var(--red-deep));color:#fff;font-weight:800;display:flex;align-items:center;justify-content:center;white-space:nowrap}
.logo{display:flex;align-items:center;gap:3px;color:var(--blue);font-weight:700;line-height:1.05;white-space:nowrap}
.logo-mark{width:1.3em;height:1.3em;background:var(--red);flex:none}

.title{left:0;right:0;text-align:center;font-weight:900;color:var(--red);white-space:nowrap;transform:translateY(-50%);letter-spacing:-.01em;line-height:1}
.title .alt{color:var(--blue)}

.perks{list-style:none;color:var(--ink);font-weight:600;line-height:1.15}
.perks li{position:relative;padding-left:1.35em}
.perks li::before{content:"";position:absolute;left:0;top:.12em;width:.85em;height:.85em;border-radius:50%;background:var(--blue);border:1.5px solid #fff;box-shadow:0 0 0 1px var(--blue)}

.photo{border:2px solid #fff;box-shadow:0 2px 6px rgba(0,0,0,.25)}
.ph-zip{background:linear-gradient(105deg,#a9bccb 0%,#3a3a3e 28%,#262629 60%,#8d4636 78%,#b56a54 100%)}
.ph-awn{background:linear-gradient(160deg,#7fa9d6 0%,#dfe3e6 38%,#2f2f31 58%,#eeeeee 72%,#aeb7bf 100%)}
.ph-rol{background:linear-gradient(180deg,#f0f0ee 0%,#6a6a6c 22%,#343436 55%,#c9c5bd 100%)}
.ph-sec{background:linear-gradient(95deg,#e8e8e8 0%,#8e9092 30%,#2a2b2d 55%,#dcdcdc 72%,#1f1f21 100%)}
.ph-pla{background:linear-gradient(180deg,#c9ccd0 0%,#eef0f1 35%,#9ea3a8 62%,#7b6552 100%)}
.ph-bli{background:linear-gradient(100deg,#f2f2f2 0%,#5a5c60 25%,#3e4044 55%,#d9a99e 85%,#ecd0c8 100%)}

.badge{width:var(--d);height:calc(var(--d)*1.22);isolation:isolate}
.badge::before,.badge::after{content:"";position:absolute;bottom:0;width:26%;height:42%;background:var(--blue);clip-path:polygon(0 0,100% 0,100% 100%,50% 78%,0 100%);z-index:-1}
.badge::before{left:22%;transform:rotate(12deg)}
.badge::after{right:22%;transform:rotate(-12deg)}
.seal{width:var(--d);height:var(--d);border-radius:50%;background:radial-gradient(circle at 40% 35%,#f0353b,#b7111a);border:calc(var(--d)*.055) solid #fff;box-shadow:0 2px 5px rgba(0,0,0,.35);display:flex;flex-direction:column;align-items:center;justify-content:center;color:#fff;line-height:1;text-align:center}
.b-top,.b-bot{font-size:calc(var(--d)*.072);font-weight:700;letter-spacing:.02em}
.b-num{font-size:calc(var(--d)*.4);font-weight:900;margin:1px 0 0}
.b-yrs{font-size:calc(var(--d)*.14);font-weight:800;margin-bottom:1px}

.offer{display:flex;align-items:stretch;gap:4px;line-height:.92;font-weight:900}
.upto{writing-mode:vertical-rl;transform:rotate(180deg);background:var(--red);color:#fff;font-weight:700;font-size:.36em;padding:3px 2px;border-radius:2px;text-align:center}
.amt{display:flex;flex-direction:column}
.pct{color:var(--red)}
.pct sup{font-size:.5em;vertical-align:.7em}
.off{color:var(--blue)}
.per{color:var(--blue);font-size:.32em;font-weight:800;text-align:center}
.from{background:var(--blue);color:#fff;font-weight:600;font-size:.44em;padding:2px 7px;border-radius:2px;align-self:flex-start;margin-bottom:4px;line-height:1.2}
.offer.price{flex-direction:column;gap:0}

.cta{left:0;right:0;background:linear-gradient(180deg,#ea2a30,var(--red-deep));color:#fff;font-weight:800;display:flex;align-items:center;justify-content:center;gap:5px;white-space:nowrap}
.cta .phone{display:inline-flex;align-items:center;gap:3px}
.cta svg{width:1em;height:1em}
.cta .chev{letter-spacing:-.1em;color:#ffb3b5;margin:0 4px 0 2px}
.cta .two{line-height:1;font-size:.8em}

.footer{left:0;right:0;bottom:0;background:linear-gradient(180deg,#1a7cc4,var(--blue-deep));color:#fff;display:flex;align-items:center;justify-content:center}
.pin-pill{display:inline-flex;align-items:center;gap:3px}
.pin-pill svg{width:1.4em;height:1.4em}
.pill{background:var(--red);color:#fff;border-radius:99px;font-weight:700;padding:.25em .9em;white-space:nowrap}
.addr-text{font-weight:500;white-space:nowrap}

/* ---------- 1080 x 1080 ---------- */
.sq .banner{width:65%;height:19%;font-size:19px}
.sq .logo{left:68%;top:5%;font-size:7.4px}
.sq .title{top:26%;font-size:21px}
.sq .title.long{font-size:17.5px}
.sq .perks{left:6.5%;top:34%;width:26%;font-size:7.4px}
.sq .perks li{margin-bottom:9px}
.sq .photo{left:34%;top:32%;width:57%;height:45%}
.sq .badge{--d:50px;left:75%;top:31%}
.sq .offer{left:8%;top:60%;font-size:24px}
.sq .offer.price{top:61%}
.sq .cta{top:77%;height:8%;font-size:11px}
.sq .footer{top:85%}
.sq .addr-box{display:flex;align-items:center;gap:6px;border:1px solid rgba(255,255,255,.7);border-radius:99px;padding:2px 8px 2px 3px;font-size:6.4px}

/* ---------- 1080 x 1920 ---------- */
.st .banner{width:62%;height:16%;font-family:'Oswald',sans-serif;font-weight:700;font-size:26px}
.st .logo{left:65%;top:5.5%;font-size:8.2px}
.st .title{top:18.3%;font-size:18.5px}
.st .title.long{font-size:15.5px}
.st .perks{left:11%;right:7%;top:23.5%;display:flex;font-size:8.3px}
.st .perks li{flex:1;padding-left:1.35em;margin-left:.5em}
.st .perks li+li{border-left:1px solid #b9b9b9;padding-left:1.85em}
.st .perks li+li::before{left:.45em}
.st .offer{left:12%;top:33%;font-size:20px;align-items:center;gap:5px;line-height:1}
.st .tag{background:var(--red);color:#fff;font-size:.42em;font-weight:700;padding:2px 5px;border-radius:2px}
.st .per-wrap{display:inline-flex;flex-direction:column;align-items:flex-end}
.st .photo{left:13%;top:41%;width:73%;height:36.5%}
.st .badge{--d:62px;left:62%;top:32.5%}
.st .cta{top:77.5%;height:8%;font-size:19px;gap:7px}
.st .cta .two{font-size:8.5px}
.st .footer{top:85.5%;flex-direction:column;gap:6px;font-size:9.5px}

/* ---------- 1440 x 1800 ---------- */
.pt .banner{width:67%;height:14.5%;font-size:21px}
.pt .logo{left:69%;top:3.6%;font-size:7.8px}
.pt .title{top:24%;font-size:22px}
.pt .title.long{font-size:18px}
.pt .perks{left:7%;top:32%;width:27%;font-size:8.2px}
.pt .perks li{margin-bottom:11px}
.pt .photo{left:36%;top:31%;width:54.5%;height:44%}
.pt .badge{--d:54px;left:75%;top:30%}
.pt .offer{left:8%;top:59.5%;font-size:25px}
.pt .offer.price{top:60%}
.pt .cta{top:75%;height:8%;font-size:12px}
.pt .footer{top:83%;flex-direction:column;gap:5px;font-size:8.6px}
</style>
</head>
<body>
<main class="board">

<!-- ======= 1080 x 1080 ======= -->
<article class="ad sq" style="left:104px;top:91px">
  <div class="banner">SALE NOW ON</div>
  <div class="logo"><span class="logo-mark"></span><span>Portals Drapes<br>&amp; Panels</span></div>
  <h2 class="title">ZIPSCREEN <span class="alt">BLINDS</span></h2>
  <ul class="perks"><li>Made to<br>Measure</li><li>Fully Installed</li><li>Wind, Sun &amp;<br>Insect Protection</li></ul>
  <div class="photo ph-zip" role="img" aria-label="Photo of black zipscreen blinds on a brick patio"></div>
  <div class="badge"><div class="seal"><span class="b-top">CELEBRATING</span><span class="b-num">13</span><span class="b-yrs">YEARS</span><span class="b-bot">IN BUSINESS</span></div></div>
  <div class="offer"><span class="upto">UP TO</span><span class="amt"><span class="pct">40<sup>%</sup></span><span class="off">OFF</span></span></div>
  <div class="cta">Book a FREE quote TODAY! <span class="phone"><svg viewBox="0 0 24 24"><circle cx="12" cy="12" r="12" fill="#fff"/><path fill="#0072bc" d="M8.6 6.2l1.6 2.6c.3.5.2 1.1-.2 1.5l-1 .9c.8 1.7 2.1 3 3.8 3.8l.9-1c.4-.4 1-.5 1.5-.2l2.6 1.6c.5.3.7.9.5 1.4l-.6 1.5c-.3.7-1 1.1-1.8 1-5.2-.6-9.3-4.7-9.9-9.9-.1-.8.3-1.5 1-1.8l1.5-.6c.5-.2 1.1 0 1.4.5z"/></svg>9482 1576</span></div>
  <div class="footer"><div class="addr-box"><span class="pin-pill"><svg viewBox="0 0 24 24"><path fill="#e31e24" d="M12 1a8 8 0 0 0-8 8c0 6 8 14 8 14s8-8 8-14a8 8 0 0 0-8-8z"/><circle cx="12" cy="9" r="3" fill="#fff"/></svg><span class="pill">Our showroom address</span></span><span class="addr-text">512 Upper Wattlebank Street, Fennick Vale</span></div></div>
</article>

<article class="ad sq" style="left:451px;top:91px">
  <div class="banner">SALE NOW ON</div>
  <div class="logo"><span class="logo-mark"></span><span>Portals Drapes<br>&amp; Panels</span></div>
  <h2 class="title">OUTDOOR <span class="alt">AWNINGS</span></h2>
  <ul class="perks"><li>Reduce Heat<br>&amp; Glare</li><li>Energy Saving</li><li>Custom Made</li></ul>
  <div class="photo ph-awn" role="img" aria-label="Photo of a striped outdoor awning over a window"></div>
  <div class="badge"><div class="seal"><span class="b-top">CELEBRATING</span><span class="b-num">13</span><span class="b-yrs">YEARS</span><span class="b-bot">IN BUSINESS</span></div></div>
  <div class="offer"><span class="upto">UP TO</span><span class="amt"><span class="pct">40<sup>%</sup></span><span class="off">OFF</span></span></div>
  <div class="cta">Book a FREE quote TODAY! <span class="phone"><svg viewBox="0 0 24 24"><circle cx="12" cy="12" r="12" fill="#fff"/><path fill="#0072bc" d="M8.6 6.2l1.6 2.6c.3.5.2 1.1-.2 1.5l-1 .9c.8 1.7 2.1 3 3.8 3.8l.9-1c.4-.4 1-.5 1.5-.2l2.6 1.6c.5.3.7.9.5 1.4l-.6 1.5c-.3.7-1 1.1-1.8 1-5.2-.6-9.3-4.7-9.9-9.9-.1-.8.3-1.5 1-1.8l1.5-.6c.5-.2 1.1 0 1.4.5z"/></svg>9482 1576</span></div>
  <div class="footer"><div class="addr-box"><span class="pin-pill"><svg viewBox="0 0 24 24"><path fill="#e31e24" d="M12 1a8 8 0 0 0-8 8c0 6 8 14 8 14s8-8 8-14a8 8 0 0 0-8-8z"/><circle cx="12" cy="9" r="3" fill="#fff"/></svg><span class="pill">Our showroom address</span></span><span class="addr-text">512 Upper Wattlebank Street, Fennick Vale</span></div></div>
</article>

<article class="ad sq" style="left:800px;top:91px">
  <div class="banner">SALE NOW ON</div>
  <div class="logo"><span class="logo-mark"></span><span>Portals Drapes<br>&amp; Panels</span></div>
  <h2 class="title">ROLLER <span class="alt">SHUTTERS</span></h2>
  <ul class="perks"><li>Security<br>Protection</li><li>Block Heat &amp;<br>Noise</li><li>Total Light<br>Control</li></ul>
  <div class="photo ph-rol" role="img" aria-label="Photo of a roller shutter lowered over a window"></div>
  <div class="badge"><div class="seal"><span class="b-top">CELEBRATING</span><span class="b-num">13</span><span class="b-yrs">YEARS</span><span class="b-bot">IN BUSINESS</span></div></div>
  <div class="offer"><span class="upto">UP TO</span><span class="amt"><span class="pct">40<sup>%</sup></span><span class="off">OFF</span></span></div>
  <div class="cta">Book a FREE quote TODAY! <span class="phone"><svg viewBox="0 0 24 24"><circle cx="12" cy="12" r="12" fill="#fff"/><path fill="#0072bc" d="M8.6 6.2l1.6 2.6c.3.5.2 1.1-.2 1.5l-1 .9c.8 1.7 2.1 3 3.8 3.8l.9-1c.4-.4 1-.5 1.5-.2l2.6 1.6c.5.3.7.9.5 1.4l-.6 1.5c-.3.7-1 1.1-1.8 1-5.2-.6-9.3-4.7-9.9-9.9-.1-.8.3-1.5 1-1.8l1.5-.6c.5-.2 1.1 0 1.4.5z"/></svg>9482 1576</span></div>
  <div class="footer"><div class="addr-box"><span class="pin-pill"><svg viewBox="0 0 24 24"><path fill="#e31e24" d="M12 1a8 8 0 0 0-8 8c0 6 8 14 8 14s8-8 8-14a8 8 0 0 0-8-8z"/><circle cx="12" cy="9" r="3" fill="#fff"/></svg><span class="pill">Our showroom address</span></span><span class="addr-text">512 Upper Wattlebank Street, Fennick Vale</span></div></div>
</article>

<article class="ad sq" style="left:104px;top:447px">
  <div class="banner">SALE NOW ON</div>
  <div class="logo"><span class="logo-mark"></span><span>Portals Drapes<br>&amp; Panels</span></div>
  <h2 class="title">SECURITY <span class="alt">DOORS</span></h2>
  <ul class="perks"><li>3 Point Locking</li><li>Premium Mesh</li><li>Custom Made</li></ul>
  <div class="photo ph-sec" role="img" aria-label="Photo of a black security door at a house entry"></div>
  <div class="badge"><div class="seal"><span class="b-top">CELEBRATING</span><span class="b-num">13</span><span class="b-yrs">YEARS</span><span class="b-bot">IN BUSINESS</span></div></div>
  <div class="offer price"><span class="from">FROM</span><span class="pct"><sup>$</sup>750</span></div>
  <div class="cta">ORDER NOW <span class="chev">›››››</span><span class="phone"><svg viewBox="0 0 24 24"><circle cx="12" cy="12" r="12" fill="#fff"/><path fill="#0072bc" d="M8.6 6.2l1.6 2.6c.3.5.2 1.1-.2 1.5l-1 .9c.8 1.7 2.1 3 3.8 3.8l.9-1c.4-.4 1-.5 1.5-.2l2.6 1.6c.5.3.7.9.5 1.4l-.6 1.5c-.3.7-1 1.1-1.8 1-5.2-.6-9.3-4.7-9.9-9.9-.1-.8.3-1.5 1-1.8l1.5-.6c.5-.2 1.1 0 1.4.5z"/></svg>9482 1576</span></div>
  <div class="footer"><div class="addr-box"><span class="pin-pill"><svg viewBox="0 0 24 24"><path fill="#e31e24" d="M12 1a8 8 0 0 0-8 8c0 6 8 14 8 14s8-8 8-14a8 8 0 0 0-8-8z"/><circle cx="12" cy="9" r="3" fill="#fff"/></svg><span class="pill">Our showroom address</span></span><span class="addr-text">512 Upper Wattlebank Street, Fennick Vale</span></div></div>
</article>

<article class="ad sq" style="left:451px;top:447px">
  <div class="banner">SALE NOW ON</div>
  <div class="logo"><span class="logo-mark"></span><span>Portals Drapes<br>&amp; Panels</span></div>
  <h2 class="title long">PLANTATION <span class="alt">SHUTTERS</span></h2>
  <ul class="perks"><li>Modern &amp;<br>Elegant</li><li>Light &amp; Privacy<br>Control</li><li>Durable &amp; Easy<br>Care</li></ul>
  <div class="photo ph-pla" role="img" aria-label="Photo of a bedroom with white plantation shutters"></div>
  <div class="badge"><div class="seal"><span class="b-top">CELEBRATING</span><span class="b-num">13</span><span class="b-yrs">YEARS</span><span class="b-bot">IN BUSINESS</span></div></div>
  <div class="offer"><span class="upto">FROM</span><span class="amt"><span class="pct"><sup>$</sup>299</span><span class="per">PER SQM</span></span></div>
  <div class="cta">Book a FREE quote TODAY! <span class="phone"><svg viewBox="0 0 24 24"><circle cx="12" cy="12" r="12" fill="#fff"/><path fill="#0072bc" d="M8.6 6.2l1.6 2.6c.3.5.2 1.1-.2 1.5l-1 .9c.8 1.7 2.1 3 3.8 3.8l.9-1c.4-.4 1-.5 1.5-.2l2.6 1.6c.5.3.7.9.5 1.4l-.6 1.5c-.3.7-1 1.1-1.8 1-5.2-.6-9.3-4.7-9.9-9.9-.1-.8.3-1.5 1-1.8l1.5-.6c.5-.2 1.1 0 1.4.5z"/></svg>9482 1576</span></div>
  <div class="footer"><div class="addr-box"><span class="pin-pill"><svg viewBox="0 0 24 24"><path fill="#e31e24" d="M12 1a8 8 0 0 0-8 8c0 6 8 14 8 14s8-8 8-14a8 8 0 0 0-8-8z"/><circle cx="12" cy="9" r="3" fill="#fff"/></svg><span class="pill">Our showroom address</span></span><span class="addr-text">512 Upper Wattlebank Street, Fennick Vale</span></div></div>
</article>

<article class="ad sq" style="left:800px;top:447px">
  <div class="banner">SALE NOW ON</div>
  <div class="logo"><span class="logo-mark"></span><span>Portals Drapes<br>&amp; Panels</span></div>
  <h2 class="title">BLINDS <span class="alt">&amp; SHEERS</span></h2>
  <ul class="perks"><li>Huge Range of<br>Fabrics</li><li>Modern Soft<br>Finish</li><li>Perfect for Any<br>Room</li></ul>
  <div class="photo ph-bli" role="img" aria-label="Photo of a bedroom with dark blinds and sheer curtains"></div>
  <div class="badge"><div class="seal"><span class="b-top">CELEBRATING</span><span class="b-num">13</span><span class="b-yrs">YEARS</span><span class="b-bot">IN BUSINESS</span></div></div>
  <div class="offer"><span class="upto">UP TO</span><span class="amt"><span class="pct">40<sup>%</sup></span><span class="off">OFF</span></span></div>
  <div class="cta">Book a FREE quote TODAY! <span class="phone"><svg viewBox="0 0 24 24"><circle cx="12" cy="12" r="12" fill="#fff"/><path fill="#0072bc" d="M8.6 6.2l1.6 2.6c.3.5.2 1.1-.2 1.5l-1 .9c.8 1.7 2.1 3 3.8 3.8l.9-1c.4-.4 1-.5 1.5-.2l2.6 1.6c.5.3.7.9.5 1.4l-.6 1.5c-.3.7-1 1.1-1.8 1-5.2-.6-9.3-4.7-9.9-9.9-.1-.8.3-1.5 1-1.8l1.5-.6c.5-.2 1.1 0 1.4.5z"/></svg>9482 1576</span></div>
  <div class="footer"><div class="addr-box"><span class="pin-pill"><svg viewBox="0 0 24 24"><path fill="#e31e24" d="M12 1a8 8 0 0 0-8 8c0 6 8 14 8 14s8-8 8-14a8 8 0 0 0-8-8z"/><circle cx="12" cy="9" r="3" fill="#fff"/></svg><span class="pill">Our showroom address</span></span><span class="addr-text">512 Upper Wattlebank Street, Fennick Vale</span></div></div>
</article>

<h1 class="size-label" style="top:827px">1080 X 1080 PX</h1>

<!-- ======= 1080 x 1920 ======= -->
<article class="ad st" style="left:125px;top:938px">
  <div class="banner">SALE NOW ON</div>
  <div class="logo"><span class="logo-mark"></span><span>Portals Drapes<br>&amp; Panels</span></div>
  <h2 class="title">ZIPSCREEN <span class="alt">BLINDS</span></h2>
  <ul class="perks"><li>Made to<br>Measure</li><li>Fully<br>Installed</li><li>Wind, Sun &amp;<br>Insect Protection</li></ul>
  <div class="offer"><span class="tag">UP TO</span><span class="pct">40<sup>%</sup></span><span class="off">OFF</span></div>
  <div class="photo ph-zip" role="img" aria-label="Photo of black zipscreen blinds on a brick patio"></div>
  <div class="badge"><div class="seal"><span class="b-top">CELEBRATING</span><span class="b-num">13</span><span class="b-yrs">YEARS</span><span class="b-bot">IN BUSINESS</span></div></div>
  <div class="cta"><span class="two">Book a FREE<br>quote TODAY!</span><span class="phone"><svg viewBox="0 0 24 24"><circle cx="12" cy="12" r="12" fill="#fff"/><path fill="#0072bc" d="M8.6 6.2l1.6 2.6c.3.5.2 1.1-.2 1.5l-1 .9c.8 1.7 2.1 3 3.8 3.8l.9-1c.4-.4 1-.5 1.5-.2l2.6 1.6c.5.3.7.9.5 1.4l-.6 1.5c-.3.7-1 1.1-1.8 1-5.2-.6-9.3-4.7-9.9-9.9-.1-.8.3-1.5 1-1.8l1.5-.6c.5-.2 1.1 0 1.4.5z"/></svg>9482 1576</span></div>
  <div class="footer"><span class="pin-pill"><svg viewBox="0 0 24 24"><path fill="#e31e24" d="M12 1a8 8 0 0 0-8 8c0 6 8 14 8 14s8-8 8-14a8 8 0 0 0-8-8z"/><circle cx="12" cy="9" r="3" fill="#fff"/></svg><span class="pill">Our showroom address</span></span><span class="addr-text">512 Upper Wattlebank Street, Fennick Vale</span></div>
</article>

<article class="ad st" style="left:457px;top:938px">
  <div class="banner">SALE NOW ON</div>
  <div class="logo"><span class="logo-mark"></span><span>Portals Drapes<br>&amp; Panels</span></div>
  <h2 class="title">OUTDOOR <span class="alt">AWNINGS</span></h2>
  <ul class="perks"><li>Reduce Heat<br>&amp; Glare</li><li>Energy<br>Saving</li><li>Custom<br>Made</li></ul>
  <div class="offer"><span class="tag">UP TO</span><span class="pct">40<sup>%</sup></span><span class="off">OFF</span></div>
  <div class="photo ph-awn" role="img" aria-label="Photo of a striped outdoor awning over a window"></div>
  <div class="badge"><div class="seal"><span class="b-top">CELEBRATING</span><span class="b-num">13</span><span class="b-yrs">YEARS</span><span class="b-bot">IN BUSINESS</span></div></div>
  <div class="cta"><span class="two">Book a FREE<br>quote TODAY!</span><span class="phone"><svg viewBox="0 0 24 24"><circle cx="12" cy="12" r="12" fill="#fff"/><path fill="#0072bc" d="M8.6 6.2l1.6 2.6c.3.5.2 1.1-.2 1.5l-1 .9c.8 1.7 2.1 3 3.8 3.8l.9-1c.4-.4 1-.5 1.5-.2l2.6 1.6c.5.3.7.9.5 1.4l-.6 1.5c-.3.7-1 1.1-1.8 1-5.2-.6-9.3-4.7-9.9-9.9-.1-.8.3-1.5 1-1.8l1.5-.6c.5-.2 1.1 0 1.4.5z"/></svg>9482 1576</span></div>
  <div class="footer"><span class="pin-pill"><svg viewBox="0 0 24 24"><path fill="#e31e24" d="M12 1a8 8 0 0 0-8 8c0 6 8 14 8 14s8-8 8-14a8 8 0 0 0-8-8z"/><circle cx="12" cy="9" r="3" fill="#fff"/></svg><span class="pill">Our showroom address</span></span><span class="addr-text">512 Upper Wattlebank Street, Fennick Vale</span></div>
</article>

<article class="ad st" style="left:791px;top:938px">
  <div class="banner">SALE NOW ON</div>
  <div class="logo"><span class="logo-mark"></span><span>Portals Drapes<br>&amp; Panels</span></div>
  <h2 class="title">ROLLER <span class="alt">SHUTTERS</span></h2>
  <ul class="perks"><li>Made to<br>Measure</li><li>Block Heat<br>&amp; Noise</li><li>Total Light<br>Control</li></ul>
  <div class="offer"><span class="tag">UP TO</span><span class="pct">40<sup>%</sup></span><span class="off">OFF</span></div>
  <div class="photo ph-rol" role="img" aria-label="Photo of a roller shutter lowered over a window"></div>
  <div class="badge"><div class="seal"><span class="b-top">CELEBRATING</span><span class="b-num">13</span><span class="b-yrs">YEARS</span><span class="b-bot">IN BUSINESS</span></div></div>
  <div class="cta"><span class="two">Book a FREE<br>quote TODAY!</span><span class="phone"><svg viewBox="0 0 24 24"><circle cx="12" cy="12" r="12" fill="#fff"/><path fill="#0072bc" d="M8.6 6.2l1.6 2.6c.3.5.2 1.1-.2 1.5l-1 .9c.8 1.7 2.1 3 3.8 3.8l.9-1c.4-.4 1-.5 1.5-.2l2.6 1.6c.5.3.7.9.5 1.4l-.6 1.5c-.3.7-1 1.1-1.8 1-5.2-.6-9.3-4.7-9.9-9.9-.1-.8.3-1.5 1-1.8l1.5-.6c.5-.2 1.1 0 1.4.5z"/></svg>9482 1576</span></div>
  <div class="footer"><span class="pin-pill"><svg viewBox="0 0 24 24"><path fill="#e31e24" d="M12 1a8 8 0 0 0-8 8c0 6 8 14 8 14s8-8 8-14a8 8 0 0 0-8-8z"/><circle cx="12" cy="9" r="3" fill="#fff"/></svg><span class="pill">Our showroom address</span></span><span class="addr-text">512 Upper Wattlebank Street, Fennick Vale</span></div>
</article>

<article class="ad st" style="left:125px;top:1484px">
  <div class="banner">SALE NOW ON</div>
  <div class="logo"><span class="logo-mark"></span><span>Portals Drapes<br>&amp; Panels</span></div>
  <h2 class="title">SECURITY <span class="alt">DOORS</span></h2>
  <ul class="perks"><li>3 Point<br>Locking</li><li>Premium<br>Mesh</li><li>Custom<br>Made</li></ul>
  <div class="offer"><span class="from">FROM</span><span class="pct"><sup>$</sup>750</span></div>
  <div class="photo ph-sec" role="img" aria-label="Photo of a black security door at a house entry"></div>
  <div class="badge"><div class="seal"><span class="b-top">CELEBRATING</span><span class="b-num">13</span><span class="b-yrs">YEARS</span><span class="b-bot">IN BUSINESS</span></div></div>
  <div class="cta"><span style="font-size:12px">ORDER NOW</span><span class="phone"><svg viewBox="0 0 24 24"><circle cx="12" cy="12" r="12" fill="#fff"/><path fill="#0072bc" d="M8.6 6.2l1.6 2.6c.3.5.2 1.1-.2 1.5l-1 .9c.8 1.7 2.1 3 3.8 3.8l.9-1c.4-.4 1-.5 1.5-.2l2.6 1.6c.5.3.7.9.5 1.4l-.6 1.5c-.3.7-1 1.1-1.8 1-5.2-.6-9.3-4.7-9.9-9.9-.1-.8.3-1.5 1-1.8l1.5-.6c.5-.2 1.1 0 1.4.5z"/></svg>9482 1576</span></div>
  <div class="footer"><span class="pin-pill"><svg viewBox="0 0 24 24"><path fill="#e31e24" d="M12 1a8 8 0 0 0-8 8c0 6 8 14 8 14s8-8 8-14a8 8 0 0 0-8-8z"/><circle cx="12" cy="9" r="3" fill="#fff"/></svg><span class="pill">Our showroom address</span></span><span class="addr-text">512 Upper Wattlebank Street, Fennick Vale</span></div>
</article>

<article class="ad st" style="left:457px;top:1484px">
  <div class="banner">SALE NOW ON</div>
  <div class="logo"><span class="logo-mark"></span><span>Portals Drapes<br>&amp; Panels</span></div>
  <h2 class="title long">PLANTATION <span class="alt">SHUTTERS</span></h2>
  <ul class="perks"><li>Modern &amp;<br>Elegant</li><li>Light &amp;<br>Privacy Control</li><li>Durable &amp;<br>Easy Care</li></ul>
  <div class="offer"><span class="from">FROM</span><span class="per-wrap"><span class="pct"><sup>$</sup>299</span><span class="per" style="font-size:7px">PER SQM</span></span></div>
  <div class="photo ph-pla" role="img" aria-label="Photo of a bedroom with white plantation shutters"></div>
  <div class="badge"><div class="seal"><span class="b-top">CELEBRATING</span><span class="b-num">13</span><span class="b-yrs">YEARS</span><span class="b-bot">IN BUSINESS</span></div></div>
  <div class="cta"><span class="two">Book a FREE<br>quote TODAY!</span><span class="phone"><svg viewBox="0 0 24 24"><circle cx="12" cy="12" r="12" fill="#fff"/><path fill="#0072bc" d="M8.6 6.2l1.6 2.6c.3.5.2 1.1-.2 1.5l-1 .9c.8 1.7 2.1 3 3.8 3.8l.9-1c.4-.4 1-.5 1.5-.2l2.6 1.6c.5.3.7.9.5 1.4l-.6 1.5c-.3.7-1 1.1-1.8 1-5.2-.6-9.3-4.7-9.9-9.9-.1-.8.3-1.5 1-1.8l1.5-.6c.5-.2 1.1 0 1.4.5z"/></svg>9482 1576</span></div>
  <div class="footer"><span class="pin-pill"><svg viewBox="0 0 24 24"><path fill="#e31e24" d="M12 1a8 8 0 0 0-8 8c0 6 8 14 8 14s8-8 8-14a8 8 0 0 0-8-8z"/><circle cx="12" cy="9" r="3" fill="#fff"/></svg><span class="pill">Our showroom address</span></span><span class="addr-text">512 Upper Wattlebank Street, Fennick Vale</span></div>
</article>

<article class="ad st" style="left:791px;top:1484px">
  <div class="banner">SALE NOW ON</div>
  <div class="logo"><span class="logo-mark"></span><span>Portals Drapes<br>&amp; Panels</span></div>
  <h2 class="title">BLINDS <span class="alt">&amp; SHEERS</span></h2>
  <ul class="perks"><li>Huge Range<br>of Fabrics</li><li>Modern<br>Soft Finish</li><li>Perfect for<br>Any Room</li></ul>
  <div class="offer"><span class="tag">UP TO</span><span class="pct">40<sup>%</sup></span><span class="off">OFF</span></div>
  <div class="photo ph-bli" role="img" aria-label="Photo of a bedroom with dark blinds and sheer curtains"></div>
  <div class="badge"><div class="seal"><span class="b-top">CELEBRATING</span><span class="b-num">13</span><span class="b-yrs">YEARS</span><span class="b-bot">IN BUSINESS</span></div></div>
  <div class="cta"><span style="font-size:12px">ORDER NOW</span><span class="phone"><svg viewBox="0 0 24 24"><circle cx="12" cy="12" r="12" fill="#fff"/><path fill="#0072bc" d="M8.6 6.2l1.6 2.6c.3.5.2 1.1-.2 1.5l-1 .9c.8 1.7 2.1 3 3.8 3.8l.9-1c.4-.4 1-.5 1.5-.2l2.6 1.6c.5.3.7.9.5 1.4l-.6 1.5c-.3.7-1 1.1-1.8 1-5.2-.6-9.3-4.7-9.9-9.9-.1-.8.3-1.5 1-1.8l1.5-.6c.5-.2 1.1 0 1.4.5z"/></svg>9482 1576</span></div>
  <div class="footer"><span class="pin-pill"><svg viewBox="0 0 24 24"><path fill="#e31e24" d="M12 1a8 8 0 0 0-8 8c0 6 8 14 8 14s8-8 8-14a8 8 0 0 0-8-8z"/><circle cx="12" cy="9" r="3" fill="#fff"/></svg><span class="pill">Our showroom address</span></span><span class="addr-text">512 Upper Wattlebank Street, Fennick Vale</span></div>
</article>

<h1 class="size-label" style="top:2052px">1080 X 1920 PX</h1>

<!-- ======= 1440 x 1800 ======= -->
<article class="ad pt" style="left:102px;top:2157px">
  <div class="banner">SALE NOW ON</div>
  <div class="logo"><span class="logo-mark"></span><span>Portals Drapes<br>&amp; Panels</span></div>
  <h2 class="title">ZIPSCREEN <span class="alt">BLINDS</span></h2>
  <ul class="perks"><li>Made to<br>Measure</li><li>Fully Installed</li><li>Wind, Sun &amp;<br>Insect<br>Protection</li></ul>
  <div class="photo ph-zip" role="img" aria-label="Photo of black zipscreen blinds on a brick patio"></div>
  <div class="badge"><div class="seal"><span class="b-top">CELEBRATING</span><span class="b-num">13</span><span class="b-yrs">YEARS</span><span class="b-bot">IN BUSINESS</span></div></div>
  <div class="offer"><span class="upto">UP TO</span><span class="amt"><span class="pct">40<sup>%</sup></span><span class="off">OFF</span></span></div>
  <div class="cta">Book a FREE quote TODAY! <span class="phone"><svg viewBox="0 0 24 24"><circle cx="12" cy="12" r="12" fill="#fff"/><path fill="#0072bc" d="M8.6 6.2l1.6 2.6c.3.5.2 1.1-.2 1.5l-1 .9c.8 1.7 2.1 3 3.8 3.8l.9-1c.4-.4 1-.5 1.5-.2l2.6 1.6c.5.3.7.9.5 1.4l-.6 1.5c-.3.7-1 1.1-1.8 1-5.2-.6-9.3-4.7-9.9-9.9-.1-.8.3-1.5 1-1.8l1.5-.6c.5-.2 1.1 0 1.4.5z"/></svg>9482 1576</span></div>
  <div class="footer"><span class="pin-pill"><svg viewBox="0 0 24 24"><path fill="#e31e24" d="M12 1a8 8 0 0 0-8 8c0 6 8 14 8 14s8-8 8-14a8 8 0 0 0-8-8z"/><circle cx="12" cy="9" r="3" fill="#fff"/></svg><span class="pill">Our showroom address</span></span><span class="addr-text">512 Upper Wattlebank Street, Fennick Vale</span></div>
</article>

<article class="ad pt" style="left:443px;top:2157px">
  <div class="banner">SALE NOW ON</div>
  <div class="logo"><span class="logo-mark"></span><span>Portals Drapes<br>&amp; Panels</span></div>
  <h2 class="title">OUTDOOR <span class="alt">AWNINGS</span></h2>
  <ul class="perks"><li>Reduce Heat<br>&amp; Glare</li><li>Energy<br>Saving</li><li>Custom Made</li></ul>
  <div class="photo ph-awn" role="img" aria-label="Photo of a striped outdoor awning over a window"></div>
  <div class="badge"><div class="seal"><span class="b-top">CELEBRATING</span><span class="b-num">13</span><span class="b-yrs">YEARS</span><span class="b-bot">IN BUSINESS</span></div></div>
  <div class="offer"><span class="upto">UP TO</span><span class="amt"><span class="pct">40<sup>%</sup></span><span class="off">OFF</span></span></div>
  <div class="cta">Book a FREE quote TODAY! <span class="phone"><svg viewBox="0 0 24 24"><circle cx="12" cy="12" r="12" fill="#fff"/><path fill="#0072bc" d="M8.6 6.2l1.6 2.6c.3.5.2 1.1-.2 1.5l-1 .9c.8 1.7 2.1 3 3.8 3.8l.9-1c.4-.4 1-.5 1.5-.2l2.6 1.6c.5.3.7.9.5 1.4l-.6 1.5c-.3.7-1 1.1-1.8 1-5.2-.6-9.3-4.7-9.9-9.9-.1-.8.3-1.5 1-1.8l1.5-.6c.5-.2 1.1 0 1.4.5z"/></svg>9482 1576</span></div>
  <div class="footer"><span class="pin-pill"><svg viewBox="0 0 24 24"><path fill="#e31e24" d="M12 1a8 8 0 0 0-8 8c0 6 8 14 8 14s8-8 8-14a8 8 0 0 0-8-8z"/><circle cx="12" cy="9" r="3" fill="#fff"/></svg><span class="pill">Our showroom address</span></span><span class="addr-text">512 Upper Wattlebank Street, Fennick Vale</span></div>
</article>

<article class="ad pt" style="left:786px;top:2157px">
  <div class="banner">SALE NOW ON</div>
  <div class="logo"><span class="logo-mark"></span><span>Portals Drapes<br>&amp; Panels</span></div>
  <h2 class="title">ROLLER <span class="alt">SHUTTERS</span></h2>
  <ul class="perks"><li>Security<br>Protection</li><li>Block Heat &amp;<br>Noise</li><li>Total Light<br>Control</li></ul>
  <div class="photo ph-rol" role="img" aria-label="Photo of a roller shutter lowered over a window"></div>
  <div class="badge"><div class="seal"><span class="b-top">CELEBRATING</span><span class="b-num">13</span><span class="b-yrs">YEARS</span><span class="b-bot">IN BUSINESS</span></div></div>
  <div class="offer"><span class="upto">UP TO</span><span class="amt"><span class="pct">40<sup>%</sup></span><span class="off">OFF</span></span></div>
  <div class="cta">Book a FREE quote TODAY! <span class="phone"><svg viewBox="0 0 24 24"><circle cx="12" cy="12" r="12" fill="#fff"/><path fill="#0072bc" d="M8.6 6.2l1.6 2.6c.3.5.2 1.1-.2 1.5l-1 .9c.8 1.7 2.1 3 3.8 3.8l.9-1c.4-.4 1-.5 1.5-.2l2.6 1.6c.5.3.7.9.5 1.4l-.6 1.5c-.3.7-1 1.1-1.8 1-5.2-.6-9.3-4.7-9.9-9.9-.1-.8.3-1.5 1-1.8l1.5-.6c.5-.2 1.1 0 1.4.5z"/></svg>9482 1576</span></div>
  <div class="footer"><span class="pin-pill"><svg viewBox="0 0 24 24"><path fill="#e31e24" d="M12 1a8 8 0 0 0-8 8c0 6 8 14 8 14s8-8 8-14a8 8 0 0 0-8-8z"/><circle cx="12" cy="9" r="3" fill="#fff"/></svg><span class="pill">Our showroom address</span></span><span class="addr-text">512 Upper Wattlebank Street, Fennick Vale</span></div>
</article>

<article class="ad pt" style="left:102px;top:2596px">
  <div class="banner">SALE NOW ON</div>
  <div class="logo"><span class="logo-mark"></span><span>Portals Drapes<br>&amp; Panels</span></div>
  <h2 class="title">SECURITY <span class="alt">DOORS</span></h2>
  <ul class="perks"><li>3 Point<br>Locking</li><li>Premium<br>Mesh</li><li>Custom Made</li></ul>
  <div class="photo ph-sec" role="img" aria-label="Photo of a black security door at a house entry"></div>
  <div class="badge"><div class="seal"><span class="b-top">CELEBRATING</span><span class="b-num">13</span><span class="b-yrs">YEARS</span><span class="b-bot">IN BUSINESS</span></div></div>
  <div class="offer price"><span class="from">FROM</span><span class="pct"><sup>$</sup>750</span></div>
  <div class="cta">ORDER NOW <span class="chev">›››››</span><span class="phone"><svg viewBox="0 0 24 24"><circle cx="12" cy="12" r="12" fill="#fff"/><path fill="#0072bc" d="M8.6 6.2l1.6 2.6c.3.5.2 1.1-.2 1.5l-1 .9c.8 1.7 2.1 3 3.8 3.8l.9-1c.4-.4 1-.5 1.5-.2l2.6 1.6c.5.3.7.9.5 1.4l-.6 1.5c-.3.7-1 1.1-1.8 1-5.2-.6-9.3-4.7-9.9-9.9-.1-.8.3-1.5 1-1.8l1.5-.6c.5-.2 1.1 0 1.4.5z"/></svg>9482 1576</span></div>
  <div class="footer"><span class="pin-pill"><svg viewBox="0 0 24 24"><path fill="#e31e24" d="M12 1a8 8 0 0 0-8 8c0 6 8 14 8 14s8-8 8-14a8 8 0 0 0-8-8z"/><circle cx="12" cy="9" r="3" fill="#fff"/></svg><span class="pill">Our showroom address</span></span><span class="addr-text">512 Upper Wattlebank Street, Fennick Vale</span></div>
</article>

<article class="ad pt" style="left:443px;top:2596px">
  <div class="banner">SALE NOW ON</div>
  <div class="logo"><span class="logo-mark"></span><span>Portals Drapes<br>&amp; Panels</span></div>
  <h2 class="title long">PLANTATION <span class="alt">SHUTTERS</span></h2>
  <ul class="perks"><li>Modern &amp;<br>Elegant</li><li>Light &amp; Privacy<br>Control</li><li>Durable &amp; Easy<br>Care</li></ul>
  <div class="photo ph-pla" role="img" aria-label="Photo of a bedroom with white plantation shutters"></div>
  <div class="badge"><div class="seal"><span class="b-top">CELEBRATING</span><span class="b-num">13</span><span class="b-yrs">YEARS</span><span class="b-bot">IN BUSINESS</span></div></div>
  <div class="offer"><span class="upto">FROM</span><span class="amt"><span class="pct"><sup>$</sup>299</span><span class="per">PER SQM</span></span></div>
  <div class="cta">Book a FREE quote TODAY! <span class="phone"><svg viewBox="0 0 24 24"><circle cx="12" cy="12" r="12" fill="#fff"/><path fill="#0072bc" d="M8.6 6.2l1.6 2.6c.3.5.2 1.1-.2 1.5l-1 .9c.8 1.7 2.1 3 3.8 3.8l.9-1c.4-.4 1-.5 1.5-.2l2.6 1.6c.5.3.7.9.5 1.4l-.6 1.5c-.3.7-1 1.1-1.8 1-5.2-.6-9.3-4.7-9.9-9.9-.1-.8.3-1.5 1-1.8l1.5-.6c.5-.2 1.1 0 1.4.5z"/></svg>9482 1576</span></div>
  <div class="footer"><span class="pin-pill"><svg viewBox="0 0 24 24"><path fill="#e31e24" d="M12 1a8 8 0 0 0-8 8c0 6 8 14 8 14s8-8 8-14a8 8 0 0 0-8-8z"/><circle cx="12" cy="9" r="3" fill="#fff"/></svg><span class="pill">Our showroom address</span></span><span class="addr-text">512 Upper Wattlebank Street, Fennick Vale</span></div>
</article>

<article class="ad pt" style="left:786px;top:2596px">
  <div class="banner">SALE NOW ON</div>
  <div class="logo"><span class="logo-mark"></span><span>Portals Drapes<br>&amp; Panels</span></div>
  <h2 class="title">BLINDS <span class="alt">&amp; SHEERS</span></h2>
  <ul class="perks"><li>Huge Range of<br>Fabrics</li><li>Modern Soft<br>Finish</li><li>Perfect for Any<br>Room</li></ul>
  <div class="photo ph-bli" role="img" aria-label="Photo of a bedroom with dark blinds and sheer curtains"></div>
  <div class="badge"><div class="seal"><span class="b-top">CELEBRATING</span><span class="b-num">13</span><span class="b-yrs">YEARS</span><span class="b-bot">IN BUSINESS</span></div></div>
  <div class="offer"><span class="upto">UP TO</span><span class="amt"><span class="pct">40<sup>%</sup></span><span class="off">OFF</span></span></div>
  <div class="cta">Book a FREE quote TODAY! <span class="phone"><svg viewBox="0 0 24 24"><circle cx="12" cy="12" r="12" fill="#fff"/><path fill="#0072bc" d="M8.6 6.2l1.6 2.6c.3.5.2 1.1-.2 1.5l-1 .9c.8 1.7 2.1 3 3.8 3.8l.9-1c.4-.4 1-.5 1.5-.2l2.6 1.6c.5.3.7.9.5 1.4l-.6 1.5c-.3.7-1 1.1-1.8 1-5.2-.6-9.3-4.7-9.9-9.9-.1-.8.3-1.5 1-1.8l1.5-.6c.5-.2 1.1 0 1.4.5z"/></svg>9482 1576</span></div>
  <div class="footer"><span class="pin-pill"><svg viewBox="0 0 24 24"><path fill="#e31e24" d="M12 1a8 8 0 0 0-8 8c0 6 8 14 8 14s8-8 8-14a8 8 0 0 0-8-8z"/><circle cx="12" cy="9" r="3" fill="#fff"/></svg><span class="pill">Our showroom address</span></span><span class="addr-text">512 Upper Wattlebank Street, Fennick Vale</span></div>
</article>

<h1 class="size-label" style="top:3061px">1440 X 1800 PX</h1>

</main>
</body>
</html>
```